We are a small NZ based company looking to rebrand our eco chem free cleaning product Brisko

This product was launched in 2021. The brand and labeling were aimed at the consumer who cared that the cleaning products they bought into their home were not only effective but non-harmful to their families and the environment. The label was a little bohemian/ natural. We feel that the labels now need to be more chic and classy, They need to look stylish in a country cottage as well as a high end minimalist home. Colours need to be mute so as to fit with most decors.
We need help with font colour and type - layout and balance. Trigger/ pump colour.
I have attached photos of our current range and labels
A couple of mock ups we are working on - (struggling with )
A colour pallet
The two last PNG files are closer to where we want to end up but they are not really right.

The products are sold online only
Our website is www.brisko.co.nz
The Brand board that we had done sometime ago is that last file.
Most of the colours on the labels are ok - except the apricot on the foaming hand soap bottle and the colour on the all purpose bottle - neither of which we love.
The Fair Harbour bottles are closer to what we are thinking.
Canva Links
https://www.draftpad.example/design/QWRTyu12abc/pLmNoPqRsTuVwXyZ12AbCd/edit
https://www.draftpad.example/design/QWRTzk34def/hGfEdCbAzYxWvUtSr34EfG/edit
https://www.draftpad.example/design/QWRTmn56ghi/tRsQpOnMlKjIhGfE56HiJk/edit
https://www.draftpad.example/design/QWRTbv78jkl/mNbVcXzLkJhGfDsA78LmNo/edit

Target Market(s)

Mothers who care about the products they bring into there homes but also want the product to look good in the home

Industry/Entity Type

Cleaning products

Requirements
Must have
• Design must be chic - and be able to sit and look great in any modern bathroom or kitchen.

```html
<!DOCTYPE html>
<html lang="en">
<head>
<meta charset="utf-8">
<title>Brisko Label Range</title>
<link rel="stylesheet" href="https://fonts.googleapis.com/css2?family=Archivo:wdth,wght@125,800&family=Figtree:wght@400;500&display=swap">
<style>
  :root {
    --canvas: #f7f8f8;
    --label-glass: #e4ecee;
    --teal: #5e8b8d;
    --teal-band: #6e9597;
    --blush: #c49690;
    --blush-band: #cba39e;
    --ink: #4d5354;
    --brand-ink: #5a5f60;
    --white: #ffffff;
  }
  * { box-sizing: border-box; margin: 0; padding: 0; }
  html, body {
    width: 1200px; height: 800px; overflow: hidden;
    background: var(--canvas);
    font-family: "Figtree", "Helvetica Neue", Arial, sans-serif;
  }
  .canvas { position: relative; width: 1200px; height: 800px; }

  .label {
    position: absolute;
    background: var(--label-glass);
    border-radius: 6px;
    overflow: hidden;
  }
  .label--laundry { left: 230px; top: 310px; width: 270px; height: 360px; }
  .label--all-purpose { left: 678px; top: 320px; width: 262px; height: 300px; }

  .brand { position: absolute; }
  .brand__lockup { display: flex; align-items: center; gap: 5px; }
  .brand__dot { width: 7px; height: 7px; border-radius: 50%; background: var(--brand-ink); }
  .brand__name { font-size: 18px; font-weight: 400; color: var(--brand-ink); line-height: 1; }
  .brand__tagline {
    display: block; font-size: 5px; letter-spacing: 0.3px;
    color: var(--brand-ink); margin-top: 3px; text-transform: uppercase;
  }
  .label--laundry .brand { left: 16px; top: 44px; }
  .label--all-purpose .brand { left: 12px; top: 42px; }
  .label--all-purpose .brand__name { font-size: 16px; }

  .product-title {
    position: absolute;
    font-family: "Archivo", "Arial Black", sans-serif;
    font-stretch: 125%;
    font-weight: 800;
    text-align: right;
    line-height: 1.02;
    letter-spacing: -1px;
  }
  .label--laundry .product-title { left: 12px; width: 242px; top: 122px; font-size: 44px; color: var(--teal); }
  .label--all-purpose .product-title { left: 8px; width: 248px; top: 110px; font-size: 32px; color: var(--blush); }

  .band {
    position: absolute; left: 0; right: 0;
    color: var(--white);
    display: flex; align-items: center;
  }
  .label--laundry .band {
    top: 253px; height: 34px; background: var(--teal-band);
    padding-left: 10px; font-size: 9.4px; white-space: nowrap;
  }
  .label--all-purpose .band {
    top: 210px; height: 36px; background: var(--blush-band);
    padding: 0 40px 0 34px; font-size: 7.6px; line-height: 1.35;
  }
  .band__size {
    position: absolute; right: -18px; top: 50%; transform: translateY(-50%);
    width: 44px; height: 44px; border-radius: 50%;
    background: var(--blush-band);
    font-size: 10px; font-weight: 500;
    display: flex; align-items: center; padding-left: 6px;
  }

  .uses { position: absolute; color: var(--ink); }
  .uses__row { display: flex; white-space: nowrap; }
  .uses__row span + span { border-left: 1px solid var(--ink); padding-left: 4px; margin-left: 5px; }
  .uses__row--ruled { border-bottom: 1px solid var(--ink); padding-bottom: 1px; }
  .label--laundry .uses { left: 38px; top: 303px; font-size: 12.5px; line-height: 1.25; }
  .label--all-purpose .uses { left: 52px; top: 250px; font-size: 11px; line-height: 1.2; }
</style>
</head>
<body>
<main class="canvas">

  <section class="label label--laundry" aria-label="Laundry liquid label">
    <div class="brand">
      <div class="brand__lockup"><span class="brand__dot"></span><span class="brand__name">Brisko</span></div>
      <span class="brand__tagline">natural home care</span>
    </div>
    <h1 class="product-title">LAUNDRY<br>LIQUID</h1>
    <p class="band">Effective clean,harsh on dirt and gentle on your clothes</p>
    <div class="uses">
      <p class="uses__row uses__row--ruled"><span>machine</span><span>handwash</span><span>soaker</span></p>
      <p class="uses__row"><span>stain remover</span><span>hot or cold water</span></p>
    </div>
  </section>

  <section class="label label--all-purpose" aria-label="All purpose cleaner label">
    <div class="brand">
      <div class="brand__lockup"><span class="brand__dot"></span><span class="brand__name">Brisko</span></div>
      <span class="brand__tagline">natural home care</span>
    </div>
    <h1 class="product-title">ALL PURPOSE<br>CLEANER</h1>
    <p class="band">everyday cleaning including benchtops, high chairs,<br>dishes &amp; so much more!<span class="band__size">500</span></p>
    <div class="uses">
      <p class="uses__row uses__row--ruled"><span>surfaces</span><span>stains</span><span>grease &amp; grime</span></p>
      <p class="uses__row"><span>great for everyday cleaning</span></p>
    </div>
  </section>

</main>
</body>
</html>
```